New Fernwick 4 Loop waste management business seeking web site

New project for business offering sustainable options within the waste industry.
Business called Fernwick 4 Loop
Targeting the consumer & industry professionals the web site needs to be able to accommodate both.
Needs to have a modern clean feel.
Logo being designed by another pro and will be completed early next week and will be submitted soon after to be incorporated into the web page
Links to another web page i like very much to take into consideration.

Target Market(s)

Industry professionals, consumers and producers of all waste, Food, constructruction, commercial, retail .. etc..

Industry/Entity Type

Waste Management

Coding

Coded - Design and coding required

Number of Pages Required

5+ page

Font styles to use
Serif
Script

Requirements
Must have
• Flexabilty, all pages as in examples
Nice to have
• Open to offers you guys and gals are the pro's

```html
<!DOCTYPE html>
<html lang="en">
<head>
<meta charset="utf-8">
<title>Fernwick 4 Loop</title>
<link rel="stylesheet" href="https://fonts.googleapis.com/css2?family=Montserrat:wght@300;400;700&family=Roboto:wght@300;400;500&display=swap">
<style>
:root{
  --ink:#1c1c1c;
  --text:#555;
  --muted:#888;
  --mint:#7fe8b2;
  --mint-text:#4fc488;
  --cyan:#2fd2e8;
  --orange:#f26a2d;
  --panel:#f2f2f2;
  --white:#fff;
  --line:#dcdcdc;
}
*{box-sizing:border-box;margin:0;padding:0}
html,body{width:701px;height:1200px;overflow:hidden}
body{position:relative;background:var(--white);font-family:'Roboto',sans-serif;color:var(--text);font-size:6px}
.abs{position:absolute}
.center{text-align:center;left:0;width:701px}

/* hero */
.hero{position:absolute;left:0;top:0;width:701px;height:283px;overflow:hidden;
  background:
    radial-gradient(ellipse 130px 150px at 500px 110px,rgba(190,180,165,.45),transparent 70%),
    radial-gradient(ellipse 420px 90px at 350px 270px,rgba(120,90,60,.55),transparent 75%),
    linear-gradient(180deg,#2f3230 0%,#43443f 30%,#5d5246 58%,#7a624a 78%,#4a3b2f 100%)}
.topbar{position:absolute;left:0;top:0;width:701px;height:26px;background:rgba(30,32,35,.7);border-top:2px solid var(--mint);border-bottom:1px solid rgba(255,255,255,.12)}
.topbar .phone{position:absolute;left:123px;top:8px;color:#fff;font-size:7px;display:flex;align-items:center;gap:4px}
.topbar .search{position:absolute;left:490px;top:8px;width:90px;height:11px;border-bottom:1px solid rgba(255,255,255,.35);color:#aaa;font-size:7px;display:flex;gap:4px}
.brand-mark{position:absolute;left:341px;top:60px;width:19px;height:19px;border-radius:50%;background:#fff}
.brand-name{top:105px;font-family:'Montserrat',sans-serif;font-weight:700;font-size:24px;letter-spacing:1px;color:#fff}
.tagline{top:138px;color:#fff;font-weight:300;font-size:8px;line-height:10.5px}
.rule{position:absolute;left:333px;top:170px;width:35px;height:2px;background:var(--mint)}
.video{top:182px;color:#fff;font-size:7.5px;font-weight:300;display:flex;justify-content:center;align-items:center;gap:4px}
.slide-dot{position:absolute;top:211px;width:4px;height:4px;border-radius:50%;background:#fff}
.next-btn{position:absolute;left:537px;top:127px;width:31px;height:31px;border-radius:50%;background:#fff}
.down-btn{position:absolute;left:340px;top:241px;width:21px;height:21px;border-radius:50%;border:1px solid #fff}

/* nav */
.nav{position:absolute;left:0;height:27px;width:701px;display:flex;justify-content:center;gap:16px;font-size:6.5px;color:#444}
.nav span{line-height:27px;position:relative}
.nav .active{color:var(--ink);font-weight:500}
.nav .active::after{content:"";position:absolute;left:-2px;right:-2px;bottom:0;height:1px;background:var(--ink)}
.main-nav{top:283px;background:#fff;border-bottom:1px solid var(--line)}

/* features */
.panel{position:absolute;left:0;top:310px;width:701px;height:429px;background:var(--panel)}
.feature{position:absolute;top:338px;width:120px;text-align:center}
.feature-icon{width:45px;height:45px;border-radius:50%;background:#e2e2e2;margin:0 auto;display:flex;align-items:center;justify-content:center}
.feature-icon.on{background:var(--mint)}
.feature h3{margin-top:13px;font-family:'Montserrat',sans-serif;font-weight:400;font-size:6.2px;letter-spacing:.8px;color:var(--ink)}
.feature h3 b{font-weight:700}
.feature h4{font-size:5.2px;font-weight:500;color:var(--ink);margin-top:3px}
.feature p{font-size:4.8px;line-height:7.4px;color:var(--muted);margin-top:5px;padding:0 6px}
.more{display:inline-block;margin-top:7px;font-size:4.8px;color:#444;border-bottom:1px solid #444;padding-bottom:1px}
.more.on{color:var(--mint-text);border-color:var(--mint-text)}
.divider{position:absolute;top:390px;width:1px;height:50px;background:var(--line)}

.section-title{font-family:'Montserrat',sans-serif;font-weight:300;font-size:12px;letter-spacing:1.4px;color:var(--ink)}
.section-title b{font-weight:700}
.section-sub{font-size:6px;line-height:8.5px;color:var(--muted)}

.member{position:absolute;top:564px;width:84px;text-align:center}
.photo{width:84px;height:70px}
.member h5{margin-top:8px;font-family:'Montserrat',sans-serif;font-weight:400;font-size:6.2px;letter-spacing:.7px;color:var(--ink)}
.member h5 b{font-weight:700}
.member.on h5{color:var(--mint-text)}
.member .role{font-size:5px;font-weight:500;color:var(--ink);margin-top:3px}
.member p{font-size:4.6px;line-height:7px;color:var(--muted);margin-top:2px}
.member .mail{font-size:4.3px;color:var(--mint-text);margin-top:3px}
.chips{display:flex;justify-content:center;gap:8px;margin-top:6px}
.chip{width:13px;height:13px;border-radius:50%;background:#e3e3e3}
.chip.cyan{background:var(--cyan)}
.chip.orange{background:var(--orange)}
.link-dash{position:absolute;top:598px;width:13px;height:1px;background:#ddd}

/* connect */
.social{position:absolute;top:810px;width:80px;text-align:center}
.social-circle{width:45px;height:45px;border-radius:50%;background:#efefef;margin:0 auto;display:flex;align-items:center;justify-content:center;font-size:5.6px;color:#333;font-weight:500}
.social-circle.on{background:var(--cyan);color:#fff}
.social .label{margin-top:10px;font-size:5px;color:#666}
.social.on .label{color:var(--cyan)}
.social .count{font-size:5px;color:var(--ink);font-weight:500;margin-top:3px}
.social-dash{position:absolute;top:832px;width:12px;height:1px;background:#ddd}

/* map */
.map{position:absolute;left:0;top:913px;width:701px;height:123px;
  background:
    radial-gradient(ellipse 160px 70px at 620px 60px,rgba(120,140,160,.55),transparent 75%),
    radial-gradient(ellipse 120px 60px at 300px 40px,rgba(150,160,170,.5),transparent 75%),
    linear-gradient(100deg,#8d9194 0%,#a4a8a9 40%,#8a9196 65%,#9aa0a4 100%)}
.contact-card{position:absolute;left:143px;top:946px;width:178px;height:55px;background:rgba(240,240,240,.9);padding:8px 12px;display:flex;gap:30px}
.contact-card h6{font-family:'Montserrat',sans-serif;font-weight:400;font-size:6.2px;letter-spacing:.7px;color:var(--ink);margin-bottom:5px}
.contact-card h6 b{font-weight:700}
.contact-card p{font-size:4.5px;line-height:6.5px;color:#333}
.contact-card .mail{color:var(--mint-text)}
.pin-ring{position:absolute;left:333px;top:958px;width:34px;height:34px;border-radius:50%;border:1px solid rgba(255,255,255,.85);background:rgba(255,255,255,.12)}
.pin-dot{position:absolute;left:348px;top:973px;width:4px;height:4px;border-radius:50%;background:#fff}

/* newsletter & footer */
.newsletter{position:absolute;left:0;top:1036px;width:701px;height:164px;background:#f4f4f4}
.field{position:absolute;left:257px;top:1103px;width:143px;height:16px;background:#fff;border:1px solid #ddd;font-size:4.8px;color:#999;padding:5px 9px}
.subscribe{position:absolute;left:401px;top:1103px;width:44px;height:16px;background:var(--mint);font-size:4.8px;font-weight:500;color:var(--ink);text-align:center;line-height:16px}
.footer-nav{top:1142px}
.footer-rule{position:absolute;left:0;top:1168px;width:701px;height:1px;background:#e4e4e4}
.to-top{position:absolute;left:535px;top:1158px;width:20px;height:20px;border-radius:50%;background:#f4f4f4;border:1px solid #e4e4e4}
.copyright{top:1177px;font-size:4.8px;line-height:7.5px;color:#666}
</style>
</head>
<body>

<header class="hero" role="img" aria-label="Hero photo of a spade turning dark soil">
  <div class="topbar">
    <div class="phone">
      <svg width="7" height="7" viewBox="0 0 24 24"><path fill="#fff" d="M6.6 10.8a15 15 0 0 0 6.6 6.6l2.2-2.2c.3-.3.7-.4 1-.2 1.1.4 2.3.6 3.6.6.6 0 1 .4 1 1V20c0 .6-.4 1-1 1A17 17 0 0 1 3 4c0-.6.4-1 1-1h3.5c.6 0 1 .4 1 1 0 1.3.2 2.5.6 3.6.1.3 0 .7-.2 1z"/></svg>
      +44(0) 141 3967021
    </div>
    <div class="search">
      <svg width="7" height="7" viewBox="0 0 24 24"><circle cx="10" cy="10" r="6" fill="none" stroke="#aaa" stroke-width="2.5"/><path d="M15 15l6 6" stroke="#aaa" stroke-width="2.5"/></svg>
      Search ...
    </div>
  </div>
  <div class="brand-mark"></div>
  <h1 class="abs center brand-name">FERNWICK 4 LOOP</h1>
  <p class="abs center tagline">Elegant and clean start up template which you can work,<br>adapting your design with ease.</p>
  <div class="rule"></div>
  <div class="abs center video">See the Video
    <svg width="10" height="10" viewBox="0 0 20 20"><circle cx="10" cy="10" r="9" fill="none" stroke="#fff" stroke-width="1.2"/><path d="M8 6l6 4-6 4z" fill="#fff"/></svg>
  </div>
  <svg class="abs" style="left:142px;top:136px" width="8" height="12" viewBox="0 0 8 12"><path d="M7 1L2 6l5 5" fill="none" stroke="#fff" stroke-width="1.3"/></svg>
  <div class="next-btn">
    <svg class="abs" style="left:12px;top:9px" width="8" height="13" viewBox="0 0 8 13"><path d="M1 1l5.5 5.5L1 12" fill="none" stroke="#222" stroke-width="1.4"/></svg>
  </div>
  <div class="slide-dot" style="left:339px;background:none;border:1px solid #fff"></div>
  <div class="slide-dot" style="left:349px"></div>
  <div class="slide-dot" style="left:359px"></div>
  <div class="down-btn">
    <svg class="abs" style="left:6px;top:7px" width="8" height="5" viewBox="0 0 8 5"><path d="M1 1l3 3 3-3" fill="none" stroke="#fff" stroke-width="1.1"/></svg>
  </div>
</header>

<nav class="nav main-nav">
  <span class="active">About</span><span>Services</span><span>Collaborations</span><span>Work</span><span>Insight</span><span>Blog</span><span>Contact</span>
</nav>

<main>
  <section class="panel"></section>

  <article class="feature" style="left:160px">
    <div class="feature-icon">
      <svg width="22" height="20" viewBox="0 0 22 20"><rect x="5" y="1" width="16" height="11" fill="none" stroke="#222" stroke-width="1.4"/><path d="M10 15h6M13 12v3" stroke="#222" stroke-width="1.4"/><rect x="1" y="8" width="6" height="11" fill="#e2e2e2" stroke="#222" stroke-width="1.4"/></svg>
    </div>
    <h3>SMALL, <b>DEDICATED TEAM</b></h3>
    <h4>Devices Support</h4>
    <p>Lorem ipsum dolor sit amet, consectetur adipisicing elit, sed do eiusmod tempor incid-idunt ut labore et dolore magna aliqua...</p>
    <span class="more">Read more ...</span>
  </article>
  <div class="divider" style="left:287px"></div>
  <article class="feature" style="left:290px">
    <div class="feature-icon">
      <svg width="18" height="22" viewBox="0 0 18 22"><rect x="4" y="1" width="13" height="17" fill="none" stroke="#222" stroke-width="1.4"/><rect x="1" y="4" width="13" height="17" fill="#e2e2e2" stroke="#222" stroke-width="1.4"/><path d="M4 9h7M4 12h7M4 15h7" stroke="#222" stroke-width="1.2"/></svg>
    </div>
    <h3>DOCUMENTATION</h3>
    <h4>User Guide</h4>
    <p>Excepteur sint occaecat cupidatat non proident, sunt in culpa qui officia deserunt mollit anim...</p>
    <span class="more">Read more ...</span>
  </article>
  <div class="divider" style="left:416px"></div>
  <article class="feature" style="left:419px">
    <div class="feature-icon on">
      <svg width="24" height="24" viewBox="0 0 24 24"><rect x="10" y="1" width="4" height="22" rx="1" transform="rotate(45 12 12)" fill="none" stroke="#222" stroke-width="1.5"/><rect x="10" y="1" width="4" height="22" rx="1" transform="rotate(-45 12 12)" fill="none" stroke="#222" stroke-width="1.5"/></svg>
    </div>
    <h3><b>SIMPLE</b> THEME OPTIONS</h3>
    <h4>Easy to Customize</h4>
    <p>Ut enim ad minim veniam, quis nostrud exercitation ullamco laboris nisi ut aliquip ex ea commodo consequat.</p>
    <span class="more on">Read more ...</span>
  </article>

  <h2 class="abs center section-title" style="top:498px">MEET OUR <b>TEAM</b></h2>
  <p class="abs center section-sub" style="top:525px">Duis aute irure dolor in reprehenderit in voluptate velit esse cillum dolore eu fugiat nulla pariatur. Excepteur sint occaecat cupid-<br>atat non proident, sunt in culpa qui officia deserunt mollit anim id est laborum.</p>

  <article class="member" style="left:144px">
    <div class="photo" role="img" aria-label="Portrait of the director in a grey suit" style="background:radial-gradient(ellipse 34px 44px at 50% 100%,#5b5d60 0%,#8c8e90 45%,transparent 80%),linear-gradient(180deg,#fafafa,#e4e4e4)"></div>
    <h5>OLIVER <b>HALE</b></h5>
    <div class="role">Director</div>
    <p>Lorem ipsum dolor sit amet, consecte-tur adipisicing elit, sed do eiusmod.</p>
    <div class="mail">hello@teamdesk.net</div>
    <div class="chips"><span class="chip"></span><span class="chip cyan"></span></div>
  </article>
  <div class="link-dash" style="left:236px"></div>
  <article class="member" style="left:253px">
    <div class="photo" role="img" aria-label="Portrait of the receptionist on a dark background" style="background:radial-gradient(ellipse 34px 44px at 50% 100%,#121212 0%,#1e1e1e 45%,transparent 80%),radial-gradient(ellipse 14px 18px at 50% 38%,#9a9a9a,transparent 80%),linear-gradient(180deg,#474747,#2c2c2c)"></div>
    <h5>MARIA <b>PENROSE</b></h5>
    <div class="role">Reception</div>
    <p>Ut enim ad minim veniam, quis nos-trud exercitation ullamco laboris nisi.</p>
    <div class="mail">hello@teamdesk.net</div>
    <div class="chips"><span class="chip"></span><span class="chip"></span><span class="chip"></span></div>
  </article>
  <div class="link-dash" style="left:345px"></div>
  <article class="member on" style="left:363px">
    <div class="photo" role="img" aria-label="Portrait of the marketing manager tinted green" style="background:radial-gradient(ellipse 36px 44px at 50% 100%,#1f7a3c 0%,#3f9e5c 45%,transparent 80%),radial-gradient(ellipse 14px 18px at 50% 38%,#7fcf92,transparent 80%),linear-gradient(180deg,#f2fbf5,#d9f1e1)"></div>
    <h5>LENA <b>CORWIN</b></h5>
    <div class="role">Marketing Managment</div>
    <p>Duis aute irure dolor in reprehenderit in voluptate velit esse cillum.</p>
    <div class="mail">hello@teamdesk.net</div>
    <div class="chips"><span class="chip orange"></span><span class="chip"></span></div>
  </article>
  <div class="link-dash" style="left:455px"></div>
  <article class="member" style="left:473px">
    <div class="photo" role="img" aria-label="Portrait of the founder in a dark suit" style="background:radial-gradient(ellipse 36px 44px at 50% 100%,#222 0%,#3a3a3a 45%,transparent 80%),linear-gradient(180deg,#fbfbfb,#e8e8e8)"></div>
    <h5>PETER <b>VANCE</b></h5>
    <div class="role">Founder</div>
    <p>Excepteur sint occaecat cupidatat non proident, sunt in culpa qui officia.</p>
    <div class="mail">hello@teamdesk.net</div>
    <div class="chips"><span class="chip"></span><span class="chip"></span></div>
  </article>

  <h2 class="abs center section-title" style="top:757px">CONNECT WITH <b>BRAMBLY</b></h2>
  <p class="abs center section-sub" style="top:779px">Brambly helps connect all learners with the people and resources</p>

  <div class="social" style="left:183px"><div class="social-circle">Plazabook</div><div class="label">Like us on Plazabook</div><div class="count">+ 1654</div></div>
  <div class="social-dash" style="left:259px"></div>
  <div class="social on" style="left:267px"><div class="social-circle on">Chirper</div><div class="label">Follow us on Chirper</div><div class="count">+ 2406</div></div>
  <div class="social-dash" style="left:344px"></div>
  <div class="social" style="left:352px"><div class="social-circle">Blog</div><div class="label">Read our Blog</div><div class="count">26</div></div>
  <div class="social-dash" style="left:428px"></div>
  <div class="social" style="left:436px"><div class="social-circle">Circlehub</div><div class="label">Follow us on Circlehub</div><div class="count">+ 308</div></div>

  <section class="map" role="img" aria-label="Street map of the office surroundings by the river"></section>
  <div class="contact-card">
    <div>
      <h6>VISIT <b>US</b></h6>
      <p><b>Brambly Inc</b><br>52 W. 7th St, Suite 210<br>Lakeview CA 95012</p>
    </div>
    <div>
      <h6><b>ASSISTANCE</b></h6>
      <p>t.+44(0) 141 3967021<br>f. +01 482 731 56X<br><span class="mail">desk@reachus.net</span></p>
    </div>
  </div>
  <div class="pin-ring"></div>
  <div class="pin-dot"></div>

  <section class="newsletter"></section>
  <h2 class="abs center section-title" style="top:1062px;font-size:9.5px">SUBSCRIBE TO OUR <b>NEWSLETTER</b></h2>
  <p class="abs center section-sub" style="top:1080px">Receive news, updates, free stuff and new releases by email</p>
  <div class="field">email address...</div>
  <div class="subscribe">Subscribe</div>
</main>

<footer>
  <nav class="nav footer-nav abs">
    <span class="active">About</span><span>Services</span><span>Collaborations</span><span>Work</span><span>Insight</span><span>Blog</span><span>Contact</span>
  </nav>
  <div class="footer-rule"></div>
  <div class="to-top">
    <svg class="abs" style="left:6px;top:7px" width="7" height="4" viewBox="0 0 7 4"><path d="M1 3.5l2.5-2.5 2.5 2.5" fill="none" stroke="#bbb" stroke-width="1"/></svg>
  </div>
  <p class="abs center copyright">Copyright © 2014 Fernwick 4 Loop<br>All Rights Reserved.</p>
</footer>

</body>
</html>
```